Etiketten für Bierflasche
Zielgruppe
Wir sind eine kleine Brauerei im Ort Gaming. Auf Grund des Ortsnamens wollen wir ein Bier für Gamer abfüllen.
Aufgabenstellung
Ich benötige ein Flaschenetikett (H 90 x B 140 mm). Dieses Bier heißt 'Mondkobold'.
Bitte folgender Text sollte oben stehen:
Mondkobold
Play your own Game
Dazu passen würde ein Gamecontroller oder ähnliches.
Die Farben sollten eher etwas dunkler gehalten werden.
Das Etikett kommt auf eine Euroflasche 0,33l (siehe Bild im Anhang).
Anbei sende ich noch Designs zur Inspiration.
Alle Zusatzangaben die am Etikett stehen müssen (z.B. Zutaten, Alkoholgehalt,...) können wir zum Schluss besprechen. Darum links und rechts vom Etikett ca. 30-40 mm freilassen.

```html
<!DOCTYPE html>
<html lang="de">
<head>
<meta charset="utf-8">
<title>Mondkobold – Flaschenetikett</title>
<link rel="stylesheet" href="https://fonts.googleapis.com/css2?family=Audiowide&family=Montserrat:wght@800&display=swap">
<style>
  :root {
    --page: #ffffff;
    --space-deep: #0a1022;
    --space-navy: #14224a;
    --nebula-magenta: #7a1f63;
    --nebula-violet: #4a1f6e;
    --nebula-blue: #1f4f86;
    --ring-white: #ffffff;
    --ring-orange: #ff5a0a;
    --dot-amber: #e9a538;
    --title-top: #ffc21a;
    --title-bottom: #ff5a00;
    --claim: #ffffff;
  }
  html, body {
    margin: 0;
    padding: 0;
    width: 799px;
    height: 1200px;
    overflow: hidden;
    background: var(--page);
  }
  .canvas {
    position: relative;
    width: 799px;
    height: 1200px;
  }
  .bottle-label {
    position: absolute;
    left: 40px;
    top: 368px;
    width: 720px;
    height: 463px;
    overflow: hidden;
    background: var(--space-deep);
  }
  .space-backdrop {
    position: absolute;
    inset: 0;
    background:
      radial-gradient(ellipse 260px 200px at 690px 60px, var(--nebula-magenta) 0%, transparent 70%),
      radial-gradient(ellipse 300px 220px at 120px 420px, var(--nebula-magenta) 0%, transparent 70%),
      radial-gradient(ellipse 200px 160px at 430px 440px, var(--nebula-violet) 0%, transparent 70%),
      radial-gradient(ellipse 160px 130px at 100px 200px, var(--nebula-blue) 0%, transparent 70%),
      radial-gradient(ellipse 220px 170px at 600px 360px, var(--nebula-blue) 0%, transparent 70%),
      linear-gradient(160deg, var(--space-navy), var(--space-deep) 55%, var(--space-navy));
  }
  .label-art {
    position: absolute;
    inset: 0;
  }
  .brand-name {
    font-family: "Audiowide", "Arial Black", sans-serif;
    font-size: 50px;
    letter-spacing: 2px;
  }
  .claim {
    font-family: "Montserrat", "Arial", sans-serif;
    font-weight: 800;
    font-size: 16px;
    letter-spacing: 1.5px;
    fill: var(--claim);
  }
</style>
</head>
<body>
<main class="canvas">
  <section class="bottle-label">
    <div class="space-backdrop" role="img" aria-label="Sternenhimmel mit violetten und blauen Nebeln"></div>
    <svg class="label-art" width="720" height="463" viewBox="0 0 720 463" xmlns="http://www.w3.org/2000/svg">
      <defs>
        <linearGradient id="title-fill" x1="0" y1="0" x2="0" y2="1">
          <stop offset="0" stop-color="var(--title-top)"/>
          <stop offset="1" stop-color="var(--title-bottom)"/>
        </linearGradient>
        <filter id="ring-glow" x="-20%" y="-20%" width="140%" height="140%">
          <feGaussianBlur stdDeviation="4" result="blur"/>
          <feMerge><feMergeNode in="blur"/><feMergeNode in="SourceGraphic"/></feMerge>
        </filter>
      </defs>

      <g class="amber-dots" fill="var(--dot-amber)">
        <circle cx="167" cy="120" r="13"/>
        <circle cx="155" cy="148" r="7"/>
        <circle cx="199" cy="118" r="4"/>
        <circle cx="621" cy="224" r="38"/>
        <circle cx="583" cy="322" r="20"/>
        <circle cx="562" cy="302" r="4"/>
      </g>

      <ellipse class="orbit-ring" cx="364" cy="222" rx="212" ry="140" transform="rotate(-18 364 222)"
               fill="none" stroke="var(--ring-orange)" stroke-width="3" filter="url(#ring-glow)"/>
      <circle class="halo-ring" cx="364" cy="212" r="172"
              fill="none" stroke="var(--ring-white)" stroke-width="3" filter="url(#ring-glow)"/>

      <text class="brand-name" x="364" y="196" text-anchor="middle" fill="url(#title-fill)">MOND</text>
      <text class="brand-name" x="364" y="256" text-anchor="middle" fill="url(#title-fill)">KOBOLD</text>

      <text class="claim" x="364" y="312" text-anchor="middle">PLAY YOUR OWN GAME</text>

      <g class="controller-icons" fill="var(--claim)">
        <path d="M329 328h8v7h7v8h-7v7h-8v-7h-7v-8h7z"/>
        <circle cx="385" cy="331" r="2.6"/>
        <circle cx="385" cy="345" r="2.6"/>
        <circle cx="378" cy="338" r="2.6"/>
        <circle cx="392" cy="338" r="2.6"/>
      </g>
    </svg>
  </section>
</main>
</body>
</html>
```